Retail Pack Frozen Food Items

Hi - I would like to create a series of retail pack frozen food labels for various items. Please see the example label attacked and create an editable label file as I will be using this file for multiple products. Please include the same verbage for the safe handling with editable text. Label needs to have labels sections for the product name, establishment number , keep frozen, net weight section, Best by Date Section, Section for UPC code , and for the bottom right we can use "Packed for Corvane Foods Inc 4738 Pellow Ave Santa Clara, CA 95112" . i have also attached our logo for the upper left hand corner to use. please create one in black and white and one version using the blue logo. Again all fields will be editable as we will use this same file to create multiple labels of different products.

```html
<!DOCTYPE html>
<html lang="en">
<head>
<meta charset="utf-8">
<title>Frozen Retail Pack Label</title>
<link rel="stylesheet" href="https://fonts.googleapis.com/css2?family=Archivo:wght@700;900&family=Barlow+Semi+Condensed:wght@300;400;600&display=swap">
<style>
  :root {
    --ink: #111111;
    --brand: #236b9b;
    --paper: #ffffff;
    --stage: #ffffff;
    --upc: #ececec;
  }
  html, body {
    margin: 0;
    width: 1200px;
    height: 894px;
    overflow: hidden;
    background: var(--stage);
  }
  .label {
    position: absolute;
    left: 0;
    top: 65px;
    width: 1200px;
    height: 763px;
    background: var(--paper);
    color: var(--ink);
    font-family: Arial, "Helvetica Neue", sans-serif;
  }
  .label > * { position: absolute; margin: 0; }

  .brand {
    left: 70px; top: 118px;
    display: flex; align-items: center; gap: 10px;
    color: var(--brand);
    font-family: "Archivo", Arial, sans-serif;
    font-weight: 700;
    font-size: 26px;
    line-height: 1.05;
  }
  .brand-dot { width: 34px; height: 34px; border-radius: 50%; background: var(--brand); flex: none; }

  .product-name {
    left: 330px; width: 540px; top: 80px;
    text-align: center;
    white-space: nowrap;
    font-weight: 700;
    font-size: 70px;
    line-height: 75px;
  }

  .establishment {
    left: 927px; top: 84px; width: 215px; height: 134px;
    border: 1.5px solid var(--ink);
    border-radius: 12px;
    text-align: center;
    font-size: 21px;
    line-height: 31px;
    padding-top: 32px;
    box-sizing: border-box;
  }

  .divider { left: 46px; top: 285px; width: 1108px; height: 1px; background: var(--ink); }

  .storage {
    left: 65px; top: 312px;
    font-weight: 700; font-size: 44px; line-height: 44px;
  }

  .handling {
    left: 50px; top: 363px; width: 640px; height: 358px;
    border: 2px solid var(--ink);
    box-sizing: border-box;
    font-family: "Barlow Semi Condensed", Arial, sans-serif;
  }
  .handling-head { padding: 12px 0 8px 13px; border-bottom: 2px solid var(--ink); height: 112px; box-sizing: border-box; }
  .handling-title { margin: 0; font-weight: 600; font-size: 28px; line-height: 32px; }
  .handling-intro { margin: 0; font-weight: 400; font-size: 23.5px; line-height: 28.5px; white-space: nowrap; }
  .handling-step {
    position: absolute;
    margin: 0;
    white-space: nowrap;
    font-weight: 300; font-size: 22px; line-height: 27px;
  }
  .step-icon { position: absolute; top: 2px; }
  .step-1 .step-icon, .step-3 .step-icon { left: -56px; width: 40px; height: 66px; }
  .step-2 .step-icon, .step-4 .step-icon { left: -72px; width: 56px; height: 66px; }
  .step-1 { left: 78px; top: 138px; }
  .step-2 { left: 382px; top: 138px; }
  .step-3 { left: 78px; top: 254px; }
  .step-4 { left: 382px; top: 254px; }

  .net-weight, .best-by {
    left: 745px; font-weight: 700; font-size: 32px; line-height: 36px;
  }
  .net-weight { top: 314px; }
  .best-by { top: 371px; }

  .upc-area { left: 745px; top: 430px; width: 395px; height: 149px; background: var(--upc); }

  .packer { left: 745px; top: 598px; font-style: normal; font-size: 25px; line-height: 28.5px; }
  .packer-name { display: block; font-family: "Archivo", Arial, sans-serif; font-weight: 900; font-size: 22px; margin-bottom: 11px; }
</style>
</head>
<body>
<main class="label">
  <div class="brand"><span class="brand-dot"></span><span>Corvane<br>Foods</span></div>

  <h1 class="product-name">Pork Grade A<br>Sparerib Cut</h1>

  <div class="establishment">Establishment No:<br>EST. ###</div>

  <div class="divider"></div>

  <p class="storage">KEEP FROZEN</p>

  <section class="handling">
    <div class="handling-head">
      <h2 class="handling-title">SAFE HANDLING INSTRUCTIONS</h2>
      <p class="handling-intro">Some food products may contain bacteria that could cause<br>illness if mishandled. Follow these instructions for your safety:</p>
    </div>

    <p class="handling-step step-1">
      <svg class="step-icon" viewBox="0 0 40 66" fill="none" stroke="#111" stroke-width="2">
        <rect x="2" y="2" width="36" height="62" rx="3"/>
        <line x1="2" y1="20" x2="38" y2="20"/>
        <line x1="33" y1="34" x2="33" y2="46"/>
        <line x1="2" y1="60" x2="38" y2="60"/>
      </svg>
      Keep refrigerated or<br>frozen. Thaw in<br>refrigerator.
    </p>

    <p class="handling-step step-2">
      <svg class="step-icon" viewBox="0 0 60 70" fill="none" stroke="#111" stroke-width="1.6">
        <path d="M4 4h14v10"/>
        <path d="M14 18v18M19 18v20M24 18v16"/>
        <path d="M30 20c10-4 20 2 26 8M28 30h24M26 40h26M20 52h36M20 60h30"/>
        <circle cx="8" cy="40" r="2"/>
        <circle cx="42" cy="50" r="2"/>
      </svg>
      Wash working surfaces,<br>utensils, and hands after<br>touching raw product.
    </p>

    <p class="handling-step step-3">
      <svg class="step-icon" viewBox="0 0 40 70" fill="none" stroke="#111" stroke-width="1.6">
        <ellipse cx="20" cy="12" rx="16" ry="10"/>
        <ellipse cx="18" cy="12" rx="5" ry="3"/>
        <path d="M6 34h28M10 29l-5 5 5 5M30 29l5 5-5 5"/>
        <path d="M24 46c-8 0-12 8-8 14l-6 6M24 46l6-4M16 60c6 2 12-2 14-6"/>
      </svg>
      Keep raw meat and<br>poultry separate from<br>other foods.
    </p>

    <p class="handling-step step-4">
      <svg class="step-icon" viewBox="0 0 60 70" fill="none" stroke="#111" stroke-width="2">
        <path d="M22 4c-3 4 3 6 0 10M30 4c-3 4 3 6 0 10M38 4c-3 4 3 6 0 10"/>
        <path d="M8 22h44M12 22v14c0 8 6 10 18 10s18-2 18-10V22"/>
        <path d="M4 22h6M50 22h6"/>
        <path d="M18 60l4-8 4 8zM27 60l4-8 4 8zM36 60l4-8 4 8zM14 62h34"/>
      </svg>
      Cook thoroughly. Keep<br>hot foods hot. Refrigerate<br>leftovers immediately.
    </p>
  </section>

  <p class="net-weight">Net Wt: 16 oz (1 lb) 454 g</p>
  <p class="best-by">Best By: MM/DD/YYYY</p>

  <div class="upc-area" role="img" aria-label="Space for the UPC barcode"></div>

  <address class="packer">
    <span class="packer-name">Packed for Corvane Foods Inc</span>
    4738 Pellow Ave,<br>Santa Clara,<br>CA 95112
  </address>
</main>
</body>
</html>
```